Business Card Design

Please use the Logo for colors and styles, and create a business card using the following info:

Matthias Loeber
Web Developer

Loeber Solutions
+41 76 482 17 05
matthias@loeber-solutions.example
www.loeber-solutions.example

Download the logo at http://loeber-solutions.example/tl_files/loeber_solutions.zip

Thanks for your works!

```html
<!DOCTYPE html>
<html lang="en">
<head>
<meta charset="utf-8">
<title>Loeber Solutions – Business Card Set</title>
<link href="https://fonts.googleapis.com/css2?family=Jost:wght@400;500&display=swap" rel="stylesheet">
<style>
  :root {
    --backdrop: #d8d8d8;
    --card: #ffffff;
    --maroon: #8b1414;
    --maroon-text: #7a1010;
    --orange: #f07a10;
    --amber: #f7a51c;
    --yellow: #fcc419;
    --sky: #bfe6f5;
    --royal: #1546b8;
    --royal-deep: #0c2a86;
    --azure: #1e8ee0;
    --azure-text: #2a9ae6;
    --red: #e01818;
    --ink: #141414;
  }
  * { margin: 0; padding: 0; box-sizing: border-box; }
  html, body { width: 1200px; height: 600px; overflow: hidden; }
  body {
    background: var(--backdrop);
    position: relative;
    font-family: "Jost", "Futura", sans-serif;
  }
  .card {
    position: absolute;
    background: var(--card);
    overflow: hidden;
    box-shadow: 0 2px 6px rgba(0,0,0,.25);
  }
  .artwork { position: absolute; left: 0; width: 100%; }
  .wordmark {
    position: absolute;
    font-weight: 400;
    letter-spacing: .02em;
    white-space: nowrap;
    text-transform: uppercase;
  }
  .details { position: absolute; font-size: 11px; line-height: 13.5px; white-space: nowrap; }

  /* Landscape front */
  .landscape-front { left: 95px; top: 124px; width: 352px; height: 144px; }
  .landscape-front .artwork {
    top: 44px; height: 100px;
    background: linear-gradient(180deg, var(--yellow) 0%, var(--amber) 14%, var(--orange) 28%, var(--maroon) 46%, var(--maroon) 100%);
  }
  .landscape-front .wordmark { left: 122px; top: 102px; color: #fff; font-size: 22px; }

  /* Landscape back */
  .landscape-back { left: 95px; top: 331px; width: 352px; height: 144px; }
  .landscape-back .artwork {
    top: 0; height: 50px;
    background: linear-gradient(180deg, var(--maroon) 0%, var(--maroon) 44%, var(--orange) 62%, var(--amber) 78%, var(--yellow) 90%, var(--sky) 100%);
  }
  .landscape-back .person { left: 32px; top: 80px; color: var(--maroon-text); }
  .landscape-back .divider { position: absolute; left: 146px; top: 64px; width: 1px; height: 63px; background: var(--maroon); }
  .landscape-back .contact { left: 168px; top: 68px; color: var(--maroon-text); }

  /* Portrait band */
  .portrait-band { left: 474px; top: 124px; width: 202px; height: 351px; }
  .portrait-band .band {
    position: absolute; left: 0; top: 140px; width: 100%; height: 52px;
    background: linear-gradient(90deg, var(--royal) 0%, var(--azure) 100%);
    border-top: 2px solid var(--amber); border-bottom: 2px solid var(--amber);
  }
  .portrait-band .wordmark { left: 28px; top: 154px; color: #fff; font-size: 17px; }
  .portrait-band .details { left: 20px; top: 245px; color: var(--ink); }
  .portrait-band .accent { color: var(--azure-text); }

  /* Portrait blue */
  .portrait-blue {
    left: 689px; top: 124px; width: 201px; height: 351px;
    background: radial-gradient(circle at 70% 30%, var(--azure) 0%, var(--royal) 55%, var(--royal-deep) 100%);
  }
  .portrait-blue .logo-box { position: absolute; left: 16px; top: 166px; width: 176px; height: 33px; background: #fff; }
  .portrait-blue .wordmark { left: 24px; top: 172px; color: var(--royal-deep); font-size: 17px; }
  .portrait-blue .person { left: 15px; top: 250px; color: #fff; font-size: 11.5px; }
  .portrait-blue .contact-band {
    position: absolute; left: 0; top: 298px; width: 100%; height: 40px;
    background: linear-gradient(90deg, var(--royal), var(--azure));
  }
  .portrait-blue .contact { right: 12px; top: 298px; color: #fff; text-align: right; font-size: 10px; line-height: 12.5px; }

  /* Portrait red */
  .portrait-red { left: 904px; top: 124px; width: 200px; height: 351px; }
  .portrait-red .wordmark { left: 14px; top: 172px; color: var(--red); font-size: 15px; }
  .portrait-red .divider { position: absolute; left: 15px; top: 248px; width: 1px; height: 84px; background: var(--red); }
  .portrait-red .details { left: 25px; top: 249px; color: var(--maroon-text); }
</style>
</head>
<body>

<section class="card landscape-front">
  <div class="artwork" role="img" aria-label="Decorative flowing band artwork in yellow, orange and maroon"></div>
  <div class="wordmark">Loeber Solutions</div>
</section>

<section class="card landscape-back">
  <div class="artwork" role="img" aria-label="Decorative flowing band artwork in maroon, orange, yellow and light blue"></div>
  <div class="details person">Matthias Loeber<br>Web Developer</div>
  <div class="divider"></div>
  <div class="details contact">Loeber Solutions<br>+41 76 482 17 05<br>matthias@loeber-solutions.example<br>www.loeber-solutions.example</div>
</section>

<section class="card portrait-band">
  <div class="band"></div>
  <div class="wordmark">Loeber Solutions</div>
  <div class="details">
    <span class="accent">Matthias Loeber<br>Web Developer<br>Loeber Solutions</span><br>
    +41 76 482 17 05<br>matthias@loeber-solutions.example<br>www.loeber-solutions.example
  </div>
</section>

<section class="card portrait-blue">
  <div class="logo-box"></div>
  <div class="wordmark">Loeber Solutions</div>
  <div class="details person">Matthias Loeber<br>Web Developer<br>Loeber Solutions</div>
  <div class="contact-band"></div>
  <div class="details contact">+41 76 482 17 05<br>matthias@loeber-solutions.example<br>www.loeber-solutions.example</div>
</section>

<section class="card portrait-red">
  <div class="wordmark">Loeber Solutions</div>
  <div class="divider"></div>
  <div class="details">Matthias Loeber<br>Web Developer<br>Loeber Solutions<br>+41 76 482 17 05<br>matthias@loeber-solutions.example<br>www.loeber-solutions.example</div>
</section>

</body>
</html>
```